Trifold flyer for our dental clinic (the Bright Harbor Clinic)

The goal of this project is to design a trifold flyer for our dental clinic (the Bright Harbor Clinic). The winning design is expected to be creative, artistic and coherent with our logo.
Updates

Designs look the same

Target Market(s)

Young generation with dental need.

Industry/Entity Type

Dental Clinic

Font styles to use
Sans Serif

Colors
0355a3
85acd3
85cae6
0592cd
00a990
86cfc6
cedeed
cee9f5
cfeae6

Requirements
Must have
• See the attached sketch for content arrangement.

```html
<!DOCTYPE html>
<html lang="en">
<head>
<meta charset="utf-8">
<title>Bright Harbor Clinic – Trifold Flyer</title>
<link href="https://fonts.googleapis.com/css2?family=Montserrat:wght@400;500;600;700&family=Poppins:wght@600;700;800&display=swap" rel="stylesheet">
<style>
  :root{
    --navy:#0355a3;
    --sky:#0592cd;
    --cyan:#1fb6e8;
    --green:#00a990;
    --mint:#5cc59a;
    --teal-light:#86cfc6;
    --pale-blue:#cedeed;
    --ice:#cee9f5;
    --soft-blue:#85acd3;
    --page:#e4e4e4;
    --white:#ffffff;
    --ink:#333a40;
  }
  *{margin:0;padding:0;box-sizing:border-box}
  html,body{width:1200px;height:800px;overflow:hidden;background:var(--page)}
  body{font-family:"Montserrat",sans-serif;color:var(--ink)}
  .flyer{position:absolute;left:45px;top:20px;width:1110px;height:760px;display:flex;box-shadow:0 6px 22px rgba(0,0,0,.18)}
  .panel{position:relative;width:370px;height:760px;overflow:hidden}
  .wave{position:absolute;left:0;width:100%;display:block}
  .panel-title{position:absolute;left:0;right:0;text-align:center;font-family:"Poppins",sans-serif;font-weight:700;color:var(--white)}

  /* Meet Us */
  .meet{background:var(--white)}
  .meet .panel-title{top:44px;font-size:32px}
  .doctor{position:absolute;left:18px;right:16px;display:flex;gap:10px}
  .doctor-photo{flex:0 0 118px;height:118px;border-right:6px solid var(--green);border-top:6px solid var(--green);background:linear-gradient(160deg,#b99273,#4a3d36)}
  .doctor-photo.grey{background:linear-gradient(160deg,#b9b4ad,#3c3f44)}
  .doctor-photo.light{background:linear-gradient(160deg,#d8d2cc,#8a6d55)}
  .doctor-info{font-size:11px;line-height:1.35}
  .doctor-name{display:inline-block;background:var(--green);color:var(--white);font-weight:700;font-size:12px;padding:2px 8px;margin-top:4px;text-transform:uppercase}
  .doctor-role{font-weight:700;font-size:11.5px}
  .doctor-bio{margin-top:3px;color:#555}
  .divider{position:absolute;left:80px;right:30px;height:1px;background:#888}

  /* Reviews */
  .reviews{background:linear-gradient(180deg,var(--green),#1f9e83)}
  .reviews .panel-title{top:44px;font-size:32px}
  .review{position:absolute;left:22px;right:24px;display:flex;gap:10px;color:var(--white)}
  .quote{font-family:"Poppins",sans-serif;font-weight:800;font-size:64px;line-height:.9;color:var(--ice);flex:0 0 40px}
  .review-body{font-size:11.5px;line-height:1.4}
  .stars{display:inline-block;background:var(--white);color:var(--green);border-radius:10px;padding:0 10px;font-size:14px;letter-spacing:2px;margin-bottom:4px}
  .reviewer{display:inline-block;background:var(--white);color:var(--soft-blue);border-radius:9px;padding:1px 10px;font-size:9px;font-weight:700;margin-top:5px;line-height:1.3;text-align:center}

  /* Cover */
  .cover{background:var(--white)}
  .call{position:absolute;top:24px;left:0;right:0;text-align:center;color:var(--white);font-family:"Poppins",sans-serif;font-weight:700}
  .call small{display:block;font-size:19px}
  .call strong{display:flex;align-items:center;justify-content:center;gap:8px;font-size:30px;letter-spacing:1px}
  .brand{position:absolute;top:150px;left:26px;display:flex;align-items:center;gap:8px;font-weight:700;font-size:13px;color:var(--sky);text-transform:uppercase}
  .brand-mark{width:14px;height:14px;background:var(--sky)}
  .hero{position:absolute;top:180px;left:40px;width:312px;height:250px;border-radius:50% 50% 46% 46%/42% 42% 58% 58%;border-bottom:6px solid var(--mint);background:linear-gradient(135deg,#e7eef3 0%,#f0c9b6 35%,#e8586b 65%,#8ec8e8 100%)}
  .offers{position:absolute;top:460px;left:0;right:0;text-align:center;color:var(--navy);font-family:"Poppins",sans-serif;font-weight:800}
  .offers h2{font-size:30px;margin-bottom:10px}
  .offer{line-height:1.05;margin-bottom:14px}
  .offer .price{font-size:42px}
  .offer .label{font-size:21px}
  .aligner{position:absolute;bottom:22px;left:0;right:0;text-align:center;color:var(--white);font-weight:600;font-size:18px}
</style>
</head>
<body>
<main class="flyer">

  <section class="panel meet">
    <svg class="wave" style="top:0" width="370" height="150" viewBox="0 0 370 150" preserveAspectRatio="none">
      <path d="M0 0H370V110C280 70 160 140 0 120Z" fill="var(--mint)"/>
      <path d="M0 120C160 140 280 70 370 110V125C280 90 160 150 0 135Z" fill="var(--green)"/>
    </svg>
    <h1 class="panel-title">Meet Us</h1>

    <article class="doctor" style="top:165px">
      <div class="doctor-photo" role="img" aria-label="Portrait photo of Dr. Lena Whitcombe"></div>
      <div class="doctor-info">
        <span class="doctor-name">Lena Whitcombe,</span>
        <div>DMD, MS</div>
        <div class="doctor-role">Board Certified Orthodontist</div>
        <p class="doctor-bio">Dr. Lena Whitcombe graduated summa cum laude with a DMD from Northgate University School of Dental Medicine.</p>
      </div>
    </article>
    <div class="divider" style="top:330px"></div>

    <article class="doctor" style="top:350px">
      <div class="doctor-photo grey" role="img" aria-label="Portrait photo of Dr. Owen P. Garrick"></div>
      <div class="doctor-info">
        <span class="doctor-name">Owen P. Garrick</span>
        <div>DMD</div>
        <div class="doctor-role">Board Certified Pediatric Dentist<br>Board Certified Orthodontist</div>
        <p class="doctor-bio">Dr. Owen Garrick is Board Certified by both the National Pediatric Dental Council and the National Orthodontic Council.</p>
      </div>
    </article>
    <div class="divider" style="top:520px"></div>

    <article class="doctor" style="top:540px">
      <div class="doctor-photo light" role="img" aria-label="Portrait photo of Dr. Priya Moreland"></div>
      <div class="doctor-info">
        <span class="doctor-name">Dr. Priya Moreland,</span>
        <div>DMD</div>
        <div class="doctor-role">General Dentist</div>
        <p class="doctor-bio">Dr. Moreland earned her DMD (Doctor of Dental Medicine) from Northgate University School of Dental Medicine and has also completed a post-graduate training in advanced general practice residency.</p>
      </div>
    </article>

    <svg class="wave" style="bottom:0" width="370" height="70" viewBox="0 0 370 70" preserveAspectRatio="none">
      <path d="M0 40C120 60 250 0 370 20V70H0Z" fill="var(--mint)"/>
      <path d="M0 55C120 70 250 20 370 35V70H0Z" fill="var(--green)"/>
    </svg>
  </section>

  <section class="panel reviews">
    <svg class="wave" style="top:0" width="370" height="170" viewBox="0 0 370 170" preserveAspectRatio="none">
      <path d="M0 0H370V150C280 110 230 170 130 160C70 155 30 140 0 150Z" fill="var(--sky)"/>
      <path d="M0 0H370V120C280 90 230 140 130 130C70 125 30 110 0 120Z" fill="var(--cyan)" opacity=".5"/>
    </svg>
    <h2 class="panel-title">Reviews</h2>

    <article class="review" style="top:200px">
      <span class="quote">&ldquo;</span>
      <div class="review-body">
        <span class="stars">★★★★★</span>
        <p>Amazing place. I wish they had dental services for adults:)</p>
        <span class="reviewer">Cora Lindqvist<br>2/17/2018</span>
      </div>
    </article>

    <article class="review" style="top:300px">
      <span class="quote">&ldquo;</span>
      <div class="review-body">
        <span class="stars">★★★★★</span>
        <p>I LOVE everyone at this office!! Dr. Whitcombe is the best of the best. The office staff are always courteous and kind, even kept an eye on my granddaughter who was watching TV while I was being seen. They are professional, nice, outgoing, friendly--just what every office strives to be--they have it all!!</p>
        <span class="reviewer">Helen Ortiz<br>2/19/2018</span>
      </div>
    </article>

    <article class="review" style="top:505px">
      <span class="quote">&ldquo;</span>
      <div class="review-body">
        <span class="stars">★★★★★</span>
        <p>Both of my boys have been treated here. Great service. I recommend them to a friend.</p>
        <span class="reviewer">Paul Brennan<br>5/15/2018</span>
      </div>
    </article>

    <article class="review" style="top:615px">
      <span class="quote">&ldquo;</span>
      <div class="review-body">
        <span class="stars">★★★★★</span>
        <p>Friendly staff, pleasant atmosphere, great on time, and a very engaged doctor. Highly recommended!</p>
        <span class="reviewer">Jun Tanaka<br>5/15/2018</span>
      </div>
    </article>
  </section>

  <section class="panel cover">
    <svg class="wave" style="top:0" width="370" height="150" viewBox="0 0 370 150" preserveAspectRatio="none">
      <path d="M0 0H370V135C260 95 130 80 0 110Z" fill="var(--mint)"/>
      <path d="M0 0H370V125C260 85 130 70 0 100Z" fill="var(--sky)"/>
      <path d="M0 0H370V100C260 70 130 60 0 80Z" fill="var(--cyan)" opacity=".6"/>
    </svg>
    <div class="call">
      <small>Call us now</small>
      <strong>
        <svg width="22" height="22" viewBox="0 0 24 24" aria-hidden="true"><path d="M6.6 10.8a15.1 15.1 0 0 0 6.6 6.6l2.2-2.2a1 1 0 0 1 1-.25 11.4 11.4 0 0 0 3.6.57 1 1 0 0 1 1 1V20a1 1 0 0 1-1 1A17 17 0 0 1 3 4a1 1 0 0 1 1-1h3.5a1 1 0 0 1 1 1c0 1.25.2 2.45.57 3.57a1 1 0 0 1-.25 1z" fill="var(--white)"/></svg>
        555-204-7731
      </strong>
    </div>

    <div class="brand"><span class="brand-mark"></span>Bright Harbor Clinic</div>
    <div class="hero" role="img" aria-label="Photo of a smiling young couple embracing"></div>

    <div class="offers">
      <h2>Special Offers</h2>
      <div class="offer"><span class="price">$69</span> <span class="label">New</span><br><span class="label">patient special</span></div>
      <div class="offer"><span class="price">$99</span> <span class="label">In-office</span><br><span class="label">teeth whitening</span></div>
    </div>

    <svg class="wave" style="bottom:0" width="370" height="90" viewBox="0 0 370 90" preserveAspectRatio="none">
      <path d="M0 40C120 60 260 10 370 0V90H0Z" fill="var(--sky)"/>
      <path d="M0 55C120 70 260 25 370 15V90H0Z" fill="var(--cyan)" opacity=".5"/>
    </svg>
    <p class="aligner">25% 40% off on ClearAlign</p>
  </section>

</main>
</body>
</html>
```